Investment firm needs refreshed corporate powerpoint slides design

We need a new and refreshed powerpoint template for our corporate investment deck. We are a technology private equity group that primarily invests in fast growing software companies and we would like to reflect that in a modern and light blue / transparant / white powerpoint and fonts template. I have also attached our old investor deck as a guideline and also check out our website to get an idea of what we do and what type of companies we invested in. Please note that our website is old and so our presentation should be a refreshed "2017" modern design, not a copy / paste of our website design and graphics.
Updates

Target Market(s)

Investors such as high net worth individuals, pension funds, banks, financial advisors

Industry/Entity Type

Investment

Colors
33a6d7
85cae6
cfeae6
edf8f6
ffffff
fff3d1
86cfc6

Requirements
Must have
• We let you be creative, we trust you have seen more investment presentations before.
Nice to have
• Pre-built models, flow charts, graphs, charts, etc.
Should not have
• Fancy or edgy images, this has to be a modern, fresh and trustworthy looking powerpoint template. No stock images, if you do use stock images for background purposes please be creative! :-)

```html
<!DOCTYPE html>
<html lang="en">
<head>
<meta charset="utf-8">
<title>Norvale — Corporate Deck Template</title>
<link href="https://fonts.googleapis.com/css2?family=Libre+Baskerville&family=Montserrat:wght@400;600;700&family=Open+Sans:ital,wght@0,300;0,400;0,600;0,700;1,400&display=swap" rel="stylesheet">
<style>
:root{
  --navy:#17406d;
  --ink:#1e4c79;
  --blue:#5c9ccb;
  --sky:#8cbfdf;
  --pale:#cfe4f1;
  --teal:#86cfc6;
  --mint:#cfeae6;
  --grey:#b7babe;
  --txt:#9aa3ab;
  --page:#eef1f4;
  --rule:#dfe5ea;
}
*{box-sizing:border-box}
html,body{margin:0;width:960px;height:1200px;overflow:hidden;background:var(--page)}
.deck{display:grid;grid-template-columns:repeat(3,292px);grid-auto-rows:165px;column-gap:28px;row-gap:6.5px;padding:3px 14px}
.slide{position:relative;background:#fff;overflow:hidden;box-shadow:0 1px 3px rgba(0,0,0,.18);font-family:'Open Sans',sans-serif;color:var(--txt)}
.slide svg{position:absolute;left:0;top:0}
.a{position:absolute}
.std::before{content:"";position:absolute;left:0;top:11px;border-left:5px solid #cfd4d9;border-top:7px solid transparent;border-bottom:7px solid transparent}
.title{position:absolute;left:13px;top:11px;margin:0;font:600 13px/1.2 'Montserrat',sans-serif;color:var(--ink);border-bottom:1px solid var(--rule);padding-bottom:2px}
.brand{font:400 15px/1 'Libre Baskerville',serif;color:var(--navy);white-space:nowrap}
.hbrand{position:absolute;right:10px;top:11px}
.foot{position:absolute;left:5px;bottom:4px;font-size:3px;color:#c2c7cc}
.corner{position:absolute;right:0;bottom:0;border-left:9px solid transparent;border-bottom:9px solid #d5dadf}
.p{font-size:3.6px;line-height:1.4;color:var(--txt);margin:0}
.lbl{font-size:4.6px;font-weight:600;color:var(--ink);margin:0 0 1px}
.ph{position:absolute}
.ic{position:absolute;border-radius:50%;display:flex;align-items:center;justify-content:center}
.tag{position:absolute;height:7px;font:700 4px/7px 'Montserrat',sans-serif;color:#fff;padding-left:5px}
.tile{position:absolute;color:#fff;text-align:center;padding:4px 5px}
.tile h4{margin:0 0 2px;font-size:4.6px;font-weight:700}
.tile p{margin:0;font-size:3.4px;line-height:1.4}
.split{position:absolute;left:0;width:146px;height:55px;padding:4px 8px;color:#fff;font-size:3.8px;line-height:1.45;text-align:justify}
.person .nm{font-size:4.6px;color:var(--ink);margin:0}
.person .rl{font-size:3.4px;color:var(--blue);margin:0}
.person ul{margin:1px 0 0;padding-left:5px;font-size:3px;line-height:1.35;color:#8a939b}
</style>
</head>
<body>
<main class="deck">

<!-- 1 cover -->
<section class="slide">
  <div class="ph" role="img" aria-label="Faceted glass facade in pale blue tones" style="inset:0;background:linear-gradient(125deg,#bcd6ea 0%,#87b6d8 35%,#a9cbe4 60%,#7eafd3 100%)"></div>
  <div class="a brand" style="left:86px;top:62px;font-size:37px">Norvale</div>
</section>

<!-- 2 title slide -->
<section class="slide">
  <svg width="292" height="165" viewBox="0 0 292 165">
    <defs><linearGradient id="g2" x1="0" y1="0" x2="1" y2="1"><stop offset="0" stop-color="#d9dcdf"/><stop offset=".5" stop-color="#7d8389"/><stop offset="1" stop-color="#2e3338"/></linearGradient></defs>
    <polygon role="img" aria-label="Black and white glass and steel building" points="0,0 168,0 118,82 168,165 0,165" fill="url(#g2)"/>
    <polygon points="62,30 80,30 112,82 80,134 62,134 94,82" fill="#fff"/>
    <polygon points="178,18 238,78 178,138 118,78" fill="#8cbfdf" opacity=".9"/>
  </svg>
  <div class="a brand" style="left:150px;top:70px;font-size:17px">Norvale</div>
  <div class="a" style="right:14px;top:130px;text-align:right">
    <div style="font:700 12px 'Montserrat',sans-serif;color:var(--navy)">Your Title Goes Here</div>
    <div style="font-size:4.6px;color:var(--navy)">Your Subtitle Goes Here</div>
  </div>
</section>

<!-- 3 agenda -->
<section class="slide std">
  <h2 class="title">Our Agenda</h2><div class="hbrand brand">Norvale</div>
  <div class="a" style="left:40px;top:46px;width:95px">
    <div style="position:relative;padding-left:16px;margin-bottom:15px"><span class="a" style="left:0;top:1px;width:9px;height:9px;background:var(--blue)"></span><p class="lbl" style="font-weight:400">Agenda One</p><p class="p">Lorem ipsum dolor sit amet, consectetur adipiscing elit, sed do tempor.</p></div>
    <div style="position:relative;padding-left:16px;margin-bottom:15px"><span class="a" style="left:0;top:1px;width:9px;height:9px;background:var(--blue)"></span><p class="lbl" style="font-weight:400">Agenda Two</p><p class="p">Lorem ipsum dolor sit amet, consectetur adipiscing elit, sed do tempor.</p></div>
    <div style="position:relative;padding-left:16px"><span class="a" style="left:0;top:1px;width:9px;height:9px;background:var(--blue)"></span><p class="lbl" style="font-weight:400">Agenda Three</p><p class="p">Lorem ipsum dolor sit amet, consectetur adipiscing elit, sed do tempor.</p></div>
  </div>
  <div class="a" style="left:159px;top:46px;width:95px">
    <div style="position:relative;padding-left:16px;margin-bottom:15px"><span class="a" style="left:0;top:1px;width:9px;height:9px;background:var(--blue)"></span><p class="lbl" style="font-weight:400">Agenda Four</p><p class="p">Lorem ipsum dolor sit amet, consectetur adipiscing elit, sed do tempor.</p></div>
    <div style="position:relative;padding-left:16px;margin-bottom:15px"><span class="a" style="left:0;top:1px;width:9px;height:9px;background:var(--blue)"></span><p class="lbl" style="font-weight:400">Agenda Five</p><p class="p">Lorem ipsum dolor sit amet, consectetur adipiscing elit, sed do tempor.</p></div>
    <div style="position:relative;padding-left:16px"><span class="a" style="left:0;top:1px;width:9px;height:9px;background:var(--blue)"></span><p class="lbl" style="font-weight:400">Agenda Six</p><p class="p">Lorem ipsum dolor sit amet, consectetur adipiscing elit, sed do tempor.</p></div>
  </div>
  <div class="foot">© 2017 NORVALE. All rights reserved</div><div class="corner"></div>
</section>

<!-- 4 quote -->
<section class="slide">
  <div class="ph" role="img" aria-label="Businessman by an office window, tinted blue and teal" style="inset:0;background:linear-gradient(160deg,#9fc6dd 0%,#93cbd6 55%,#8fd1c9 100%)"></div>
  <div class="ic" style="left:133px;top:40px;width:26px;height:26px;background:#fff;color:var(--teal);font:700 20px/1 'Montserrat',sans-serif;padding-top:9px">“</div>
  <div class="a" style="left:0;right:0;top:76px;text-align:center;color:#fff;font:300 9.4px/1.25 'Open Sans',sans-serif">Coming together is a beginning.<br>Keeping together is progress.<br>Working together is success.</div>
  <div class="a" style="left:0;right:0;top:120px;text-align:center;color:#fff;font-size:4.6px">- Alden Hart -</div>
</section>

<!-- 5 divider -->
<section class="slide">
  <svg width="292" height="165" viewBox="0 0 292 165">
    <defs><linearGradient id="g5" x1="0" y1="0" x2="1" y2=".6"><stop offset="0" stop-color="#3b4046"/><stop offset=".45" stop-color="#c4c9ce"/><stop offset="1" stop-color="#5d656d"/></linearGradient></defs>
    <rect role="img" aria-label="Skyscrapers seen from below in grey tones" width="292" height="165" fill="url(#g5)"/>
    <polygon points="0,112 82,28 118,28 218,108 158,165 0,165" fill="#fff"/>
    <polygon points="0,0 32,0 0,30" fill="#fff"/>
  </svg>
  <div class="a" style="right:152px;top:104px;text-align:right">
    <div class="brand" style="font-size:17px">Norvale</div>
    <div style="font:600 10.5px 'Montserrat',sans-serif;color:var(--navy);margin-top:4px">Divider Page</div>
    <div style="font-size:4.6px;color:var(--blue)">Your Subtitle Here</div>
  </div>
</section>

<!-- 6 capital -->
<section class="slide">
  <svg width="292" height="165" viewBox="0 0 292 165">
    <defs><linearGradient id="g6" x1="0" y1="0" x2="0" y2="1"><stop offset="0" stop-color="#c9cdd1"/><stop offset=".6" stop-color="#6d747b"/><stop offset="1" stop-color="#3e454c"/></linearGradient></defs>
    <rect role="img" aria-label="City skyline seen from above" width="292" height="165" fill="url(#g6)"/>
    <polygon points="146,0 275,0 204,165 66,165" fill="#5c9ccb" opacity=".75"/>
  </svg>
  <div class="a" style="right:66px;top:78px;text-align:right;color:#fff;font:300 13px/1.3 'Open Sans',sans-serif">You Need a<br><b style="font-weight:700">Different Kind Of</b><br>Capital.</div>
</section>

<!-- 7 population -->
<section class="slide std">
  <h2 class="title">Population Chart</h2><div class="hbrand brand">Norvale</div>
  <div class="ph" role="img" aria-label="World map in blue dots" style="left:24px;top:38px;width:140px;height:60px;border-radius:18px 30px 20px 26px;background:linear-gradient(90deg,#8cbfdf,#5c9ccb 60%,#8cbfdf)"></div>
  <div class="a" style="left:176px;top:44px;width:38px;text-align:center;font-size:3.6px;color:var(--ink)">Woman</div>
  <div class="a" style="left:232px;top:44px;width:38px;text-align:center;font-size:3.6px;color:var(--ink)">Man</div>
  <svg width="292" height="165" viewBox="0 0 292 165">
    <circle cx="195" cy="70" r="16" fill="none" stroke="#e6ecf0" stroke-width="2"/>
    <circle cx="195" cy="70" r="16" fill="none" stroke="#86cfc6" stroke-width="2" stroke-dasharray="45.2 100.5" transform="rotate(-90 195 70)"/>
    <circle cx="251" cy="70" r="16" fill="none" stroke="#e6ecf0" stroke-width="2"/>
    <circle cx="251" cy="70" r="16" fill="none" stroke="#17406d" stroke-width="2" stroke-dasharray="55.3 100.5" transform="rotate(-90 251 70)"/>
    <text x="195" y="73" text-anchor="middle" font-family="Open Sans" font-size="8" fill="#86cfc6">45%</text>
    <text x="251" y="73" text-anchor="middle" font-family="Open Sans" font-weight="600" font-size="8" fill="#17406d">55%</text>
    <text x="195" y="96" text-anchor="middle" font-family="Open Sans" font-size="4.5" fill="#8a939b">1.025.000</text>
    <text x="251" y="96" text-anchor="middle" font-family="Open Sans" font-size="4.5" fill="#8a939b">1.864.000</text>
  </svg>
  <p class="a p" style="left:22px;top:116px;width:250px;font-size:3.3px">There are many variations of passages of Lorem Ipsum available, but the majority have suffered alteration in some form, by injected humour, or randomised words which don't look even slightly believable. Contrary to popular belief it has roots in a piece of classical Latin literature from long ago, making it over two thousand years old, and it remains a steady placeholder for layouts of every kind.</p>
  <div class="foot">© 2017 NORVALE. All rights reserved</div><div class="corner"></div>
</section>

<!-- 8 market performance -->
<section class="slide std">
  <h2 class="title">Market Performance</h2><div class="hbrand brand">Norvale</div>
  <svg width="292" height="165" viewBox="0 0 292 165">
    <defs><polygon id="chev" points="0,0 6,0 12,6 6,12 0,12 6,6"/></defs>
    <circle cx="29" cy="53" r="10" fill="#17406d"/><rect x="24" y="50" width="10" height="6" rx="1" fill="#fff"/>
    <circle cx="29" cy="82" r="10" fill="#5c9ccb"/><path d="M24 85 L34 79 M29 78 L31 86" stroke="#fff" stroke-width="1.6"/>
    <circle cx="29" cy="111" r="10" fill="#b7babe"/><rect x="24" y="108" width="10" height="7" rx="1" fill="#fff"/><rect x="27" y="106" width="4" height="2" fill="none" stroke="#fff" stroke-width=".8"/>
    <circle cx="29" cy="140" r="10" fill="#86cfc6"/><path d="M23 140 A6 6 0 0 1 35 140 Z" fill="#fff"/><path d="M29 140 V145" stroke="#fff" stroke-width="1"/>
    <g transform="translate(44 47)"><use href="#chev" fill="#17406d"/><use href="#chev" x="11" fill="#17406d"/><use href="#chev" x="22" fill="#17406d"/><use href="#chev" x="33" fill="#17406d"/><use href="#chev" x="44" fill="#17406d"/><use href="#chev" x="55" fill="#e1e5e9"/><use href="#chev" x="66" fill="#e1e5e9"/><use href="#chev" x="77" fill="#e1e5e9"/><use href="#chev" x="88" fill="#e1e5e9"/><use href="#chev" x="99" fill="#e1e5e9"/></g>
    <g transform="translate(44 76)"><use href="#chev" fill="#5c9ccb"/><use href="#chev" x="11" fill="#5c9ccb"/><use href="#chev" x="22" fill="#5c9ccb"/><use href="#chev" x="33" fill="#5c9ccb"/><use href="#chev" x="44" fill="#5c9ccb"/><use href="#chev" x="55" fill="#5c9ccb"/><use href="#chev" x="66" fill="#e1e5e9"/><use href="#chev" x="77" fill="#e1e5e9"/><use href="#chev" x="88" fill="#e1e5e9"/><use href="#chev" x="99" fill="#e1e5e9"/></g>
    <g transform="translate(44 105)"><use href="#chev" fill="#a3a7ab"/><use href="#chev" x="11" fill="#a3a7ab"/><use href="#chev" x="22" fill="#a3a7ab"/><use href="#chev" x="33" fill="#a3a7ab"/><use href="#chev" x="44" fill="#a3a7ab"/><use href="#chev" x="55" fill="#a3a7ab"/><use href="#chev" x="66" fill="#e1e5e9"/><use href="#chev" x="77" fill="#e1e5e9"/><use href="#chev" x="88" fill="#e1e5e9"/><use href="#chev" x="99" fill="#e1e5e9"/></g>
    <g transform="translate(44 134)"><use href="#chev" fill="#86cfc6"/><use href="#chev" x="11" fill="#86cfc6"/><use href="#chev" x="22" fill="#86cfc6"/><use href="#chev" x="33" fill="#86cfc6"/><use href="#chev" x="44" fill="#86cfc6"/><use href="#chev" x="55" fill="#e1e5e9"/><use href="#chev" x="66" fill="#e1e5e9"/><use href="#chev" x="77" fill="#e1e5e9"/><use href="#chev" x="88" fill="#e1e5e9"/><use href="#chev" x="99" fill="#e1e5e9"/></g>
    <path d="M176 46 H172 V152 H176" fill="none" stroke="#d5dadf" stroke-width=".8"/>
  </svg>
  <div class="a" style="left:188px;top:44px;width:88px">
    <div style="height:30px"><p class="lbl">Glorious</p><p class="p">Nullam eu tempor purus. Nunc a leo magna, sit amet consequat risus. Etiam faucibus tortor a ipsum vehicular.</p></div>
    <div style="height:29px"><p class="lbl">System</p><p class="p">Nullam eu tempor purus. Nunc a leo magna, sit amet consequat risus. Etiam faucibus tortor a ipsum vehicular.</p></div>
    <div style="height:29px"><p class="lbl">Market</p><p class="p">Nullam eu tempor purus. Nunc a leo magna, sit amet consequat risus. Etiam faucibus tortor a ipsum vehicular.</p></div>
    <div><p class="lbl">Diversification</p><p class="p">Nullam eu tempor purus. Nunc a leo magna, sit amet consequat risus. Etiam faucibus tortor a ipsum vehicular.</p></div>
  </div>
  <div class="foot">© 2017 NORVALE. All rights reserved</div><div class="corner"></div>
</section>

<!-- 9 company target -->
<section class="slide std">
  <h2 class="title">Company Target</h2><div class="hbrand brand">Norvale</div>
  <svg width="292" height="165" viewBox="0 0 292 165">
    <circle cx="34" cy="54" r="8" fill="#17406d"/><rect x="30" y="52" width="8" height="5" fill="#fff"/>
    <circle cx="34" cy="84" r="8" fill="#5c9ccb"/><path d="M30 83 A5 5 0 0 1 38 83 M32 85 A3 3 0 0 1 36 85" fill="none" stroke="#fff" stroke-width=".9"/>
    <circle cx="34" cy="113" r="8" fill="#b7babe"/><path d="M31 117 L34 109 L37 117" fill="none" stroke="#fff" stroke-width="1"/>
    <circle cx="34" cy="142" r="8" fill="#86cfc6"/><rect x="30" y="139" width="8" height="5" rx="1" fill="#fff"/>
    <polygon points="136,66 150,66 180,96 150,126 136,126 166,96" fill="#86cfc6"/>
    <polygon points="150,62 168,62 202,96 168,130 150,130 184,96" fill="#8cbfdf"/>
    <polygon points="166,56 188,56 228,96 188,136 166,136 206,96" fill="#5c9ccb"/>
    <polygon points="186,46 216,46 266,96 216,146 186,146 236,96" fill="#17406d"/>
  </svg>
  <div class="a" style="left:47px;top:47px;width:60px">
    <div style="height:30px"><p class="lbl" style="font-size:4px">Confusion</p><p class="p" style="font-size:3.2px">Nullam eu tempor purus. Nunc a leo magna, sit amet consequat risus.</p></div>
    <div style="height:29px"><p class="lbl" style="font-size:4px;color:var(--blue)">Intangible</p><p class="p" style="font-size:3.2px">Nullam eu tempor purus. Nunc a leo magna, sit amet consequat risus.</p></div>
    <div style="height:29px"><p class="lbl" style="font-size:4px;color:#8a939b">Perform</p><p class="p" style="font-size:3.2px">Nullam eu tempor purus. Nunc a leo magna, sit amet consequat risus.</p></div>
    <div><p class="lbl" style="font-size:4px;color:var(--teal)">Good Sales</p><p class="p" style="font-size:3.2px">Nullam eu tempor purus. Nunc a leo magna, sit amet consequat risus.</p></div>
  </div>
  <div class="foot">© 2017 NORVALE. All rights reserved</div><div class="corner"></div>
</section>

<!-- 10 european map -->
<section class="slide std">
  <h2 class="title">European Map Analisys</h2><div class="hbrand brand">Norvale</div>
  <div class="a" style="left:27px;top:48px;width:106px">
    <p class="p" style="font-size:3.2px;color:var(--sky)">Lorem text ever since the 1500s when an unknown printer took a galley.</p>
    <p class="p" style="font-size:3.2px;margin-top:2px">Of shopping carts are abandoned right before the transaction is completed. Suitable for all categories.</p>
    <p class="p" style="font-size:3.2px;margin-top:2px">For every 5 emails received, we get 2 phone calls. Suitable for all categories business and personal presentation. Suitable for all categories business and personal presentation.</p>
  </div>
  <div class="a" style="left:28px;top:97px;color:var(--teal);font:600 7px 'Open Sans',sans-serif;line-height:1">60%<div style="font-size:3px;color:var(--txt);font-weight:400;margin-bottom:3px">Female Users</div>40%<div style="font-size:3px;color:var(--txt);font-weight:400">Male Users</div></div>
  <div class="a" style="left:73px;top:99px;width:60px"><div style="font:600 7px 'Open Sans',sans-serif;color:var(--blue)">800.654</div><p class="p" style="font-size:3px">Suitable for all categories business and personal presentation. Suitable for all categories business and personal presentation.</p></div>
  <div class="ph" role="img" aria-label="Map of Europe in grey" style="left:222px;top:44px;width:64px;height:110px;border-radius:40% 20% 35% 45%;background:linear-gradient(160deg,#c9ccd0,#aeb2b6)"></div>
  <div class="tag" style="left:159px;top:47px;width:62px;background:var(--navy)">SCHEDULLE</div>
  <p class="a p" style="left:164px;top:57px;width:40px;font-size:2.8px">Suitable for all categories. Lorem ipsum dolor sit amet.</p>
  <div class="tag" style="left:169px;top:90px;width:62px;background:var(--blue)">PROCHEDURE</div>
  <p class="a p" style="left:174px;top:100px;width:40px;font-size:2.8px">Suitable for all categories. Lorem ipsum dolor sit amet.</p>
  <div class="tag" style="left:193px;top:128px;width:62px;background:var(--teal)">ANTIHIPATION</div>
  <p class="a p" style="left:198px;top:138px;width:40px;font-size:2.8px">Suitable for all categories. Lorem ipsum dolor sit amet.</p>
  <svg width="292" height="165" viewBox="0 0 292 165">
    <circle cx="253" cy="87" r="4" fill="#fff" stroke="#5d656d" stroke-width="1"/><circle cx="253" cy="87" r="1.4" fill="#5d656d"/>
    <circle cx="225" cy="66" r="3" fill="none" stroke="#17406d" stroke-width=".8"/>
    <circle cx="236" cy="104" r="3" fill="none" stroke="#5c9ccb" stroke-width=".8"/>
    <circle cx="260" cy="140" r="3" fill="none" stroke="#86cfc6" stroke-width=".8"/>
  </svg>
  <div class="foot">© 2017 NORVALE. All rights reserved</div><div class="corner"></div>
</section>

<!-- 11 performance level -->
<section class="slide std">
  <h2 class="title">Performance Level</h2><div class="hbrand brand">Norvale</div>
  <svg width="292" height="165" viewBox="0 0 292 165">
    <g fill="none" stroke-width="20">
      <circle cx="138" cy="80" r="27" stroke="#86cfc6" stroke-dasharray="40.4 129.2" transform="rotate(181 138 80)"/>
      <circle cx="138" cy="80" r="27" stroke="#17406d" stroke-dasharray="40.4 129.2" transform="rotate(271 138 80)"/>
      <circle cx="138" cy="80" r="27" stroke="#5c9ccb" stroke-dasharray="40.4 129.2" transform="rotate(1 138 80)"/>
      <circle cx="138" cy="80" r="27" stroke="#b7babe" stroke-dasharray="40.4 129.2" transform="rotate(91 138 80)"/>
    </g>
    <g font-family="Montserrat" font-weight="700" font-size="6" fill="#fff" text-anchor="middle">
      <text x="122" y="62">01</text><text x="157" y="76">01</text><text x="150" y="104">01</text><text x="115" y="90">01</text>
    </g>
    <path d="M101 58 A6 6 0 0 1 113 58 Z" fill="#86cfc6"/><path d="M107 58 V65" stroke="#86cfc6"/>
    <rect x="103" y="92" width="9" height="6" fill="#b7babe"/>
    <circle cx="200" cy="58" r="3.5" fill="none" stroke="#17406d" stroke-width="1"/><rect x="198.5" y="62" width="3" height="3" fill="#17406d"/>
    <rect x="196" y="93" width="9" height="6" fill="#5c9ccb"/>
  </svg>
  <div class="a" style="left:12px;top:55px;width:80px;text-align:right"><p class="lbl" style="font-weight:400;color:var(--teal);font-size:4px">Warning</p><p class="p" style="font-size:3.2px">Nullam eu tempor purus. Nunc a leo magna, sit amet consequat risus. Etiam faucibus tortor.</p></div>
  <div class="a" style="left:12px;top:88px;width:80px;text-align:right"><p class="lbl" style="font-weight:400;color:#8a939b;font-size:4px">Digital</p><p class="p" style="font-size:3.2px">Nullam eu tempor purus. Nunc a leo magna, sit amet consequat risus. Etiam faucibus tortor.</p></div>
  <div class="a" style="left:213px;top:55px;width:70px"><p class="lbl" style="font-size:4px">Mobile</p><p class="p" style="font-size:3.2px">Nullam eu tempor purus. Nunc a leo magna, sit amet consequat risus. Etiam faucibus tortor.</p></div>
  <div class="a" style="left:213px;top:88px;width:70px"><p class="lbl" style="font-size:4px;color:var(--blue)">Security</p><p class="p" style="font-size:3.2px">Nullam eu tempor purus. Nunc a leo magna, sit amet consequat risus. Etiam faucibus tortor.</p></div>
  <p class="a p" style="left:26px;top:139px;width:240px;text-align:center;font-style:italic;font-size:3.4px;color:var(--ink)">Lorem ipsum dolor sit amet, consectetur adipiscing elit. Sed et consectetur lacus. Sed sit amet nulla vel dolor gravida bibendum. Nunc odio massa, sodales et consectetur a, iaculis eget sapien. Mauris dignissim tortor.</p>
  <div class="foot">© 2017 NORVALE. All rights reserved</div><div class="corner"></div>
</section>

<!-- 12 master option -->
<section class="slide">
  <div class="a" style="left:0;right:0;top:2px;height:26px;background:var(--navy)"></div>
  <div class="a" style="left:0;top:8px;border-left:5px solid #5c9ccb;border-top:7px solid transparent;border-bottom:7px solid transparent"></div>
  <h2 class="a" style="left:13px;top:8px;margin:0;font:600 13px 'Montserrat',sans-serif;color:#fff">Other Option of Master Slide</h2>
  <div class="a brand" style="right:10px;top:9px;color:#fff">Norvale</div>
  <div class="foot">© 2017 NORVALE. All rights reserved</div><div class="corner"></div>
</section>

<!-- 13 photo and text grid -->
<section class="slide">
  <div class="split" style="top:0;background:#6ea7cf">Lorem ipsum dolor sit amet consectetur adipiscing elit, sed do eiusmod tempor incididunt ut labore et dolore magna aliqua. Ut enimad minim veniam, quis nostrud exercitation ullamco laboris nisi ut aliquip ex ea commodo consequat.</div>
  <div class="ph" role="img" aria-label="City skyline at dusk" style="left:146px;top:0;width:146px;height:55px;background:linear-gradient(180deg,#8e949a,#4b5259)"></div>
  <div class="ph" role="img" aria-label="Aerial view of city towers" style="left:0;top:55px;width:146px;height:55px;background:linear-gradient(180deg,#b9bec3,#6d747b)"></div>
  <div class="split" style="top:55px;left:146px;background:#b5b8bb">Lorem ipsum dolor sit amet consectetur adipiscing elit, sed do eiusmod tempor incididunt ut labore et dolore magna aliqua. Ut enimad minim veniam, quis nostrud exercitation ullamco laboris nisi ut aliquip ex ea commodo consequat.</div>
  <div class="split" style="top:110px;background:#86cfc6">Lorem ipsum dolor sit amet consectetur adipiscing elit, sed do eiusmod tempor incididunt ut labore et dolore magna aliqua. Ut enimad minim veniam, quis nostrud exercitation ullamco laboris nisi ut aliquip ex ea commodo consequat.</div>
  <div class="ph" role="img" aria-label="Glass skyscrapers from below" style="left:146px;top:110px;width:146px;height:55px;background:linear-gradient(135deg,#6b737b,#c7ccd1 50%,#5a626a)"></div>
</section>

<!-- 14 mockup -->
<section class="slide">
  <div class="ph" role="img" aria-label="Blue technology circuitry background" style="left:0;top:0;width:292px;height:80px;background:linear-gradient(120deg,#3f86bd,#6aa8d3 50%,#c3d7e6)"></div>
  <div class="a" style="left:14px;top:10px;color:#fff;font:400 11px 'Montserrat',sans-serif">OUR MOCKUP</div>
  <div class="a" style="left:8px;top:36px;color:#fff;font-size:6px">Heading Here</div>
  <p class="a" style="left:8px;top:45px;width:112px;margin:0;color:#fff;font-size:3.4px;line-height:1.4">Lorem ipsum dolor sit amet, consectetur adipiscing elit, sed do eiusmod tempor incididunt ut labore et dolore magna aliqua. Ut enimad minim veniam, quis nostrud exercitation ullamco laboris nisi ut aliquip ex ea commodo consequat duis.</p>
  <div class="a" style="left:129px;top:13px;width:156px;height:100px;background:#1b1e21;border-radius:3px;padding:4px">
    <div style="width:100%;height:86px;background:#fff;display:flex;align-items:center;justify-content:center"><span class="brand" style="font-size:25px">Norvale</span></div>
  </div>
  <div class="a" style="left:196px;top:113px;width:22px;height:12px;background:linear-gradient(#c9cdd1,#e2e5e8)"></div>
  <div class="a" style="left:182px;top:124px;width:50px;height:3px;border-radius:2px;background:#d5d9dd"></div>
  <div class="a" style="left:10px;top:88px;width:112px">
    <div style="position:relative;padding-left:14px;height:25px"><span class="ic" style="left:0;top:1px;width:8px;height:8px;background:var(--blue)"></span><p class="p" style="font-size:3.4px">Lorem ipsum dolor sit amet, consectetur adipiscing elit, sed do eiusmod tempor incididunt ut labore et dolore magna aliqua minim veniam, quis nostrud.</p></div>
    <div style="position:relative;padding-left:14px;height:25px"><span class="ic" style="left:0;top:1px;width:8px;height:8px;background:var(--blue)"></span><p class="p" style="font-size:3.4px">Lorem ipsum dolor sit amet, consectetur adipiscing elit, sed do eiusmod tempor incididunt ut labore et dolore magna aliqua minim veniam, quis nostrud.</p></div>
    <div style="position:relative;padding-left:14px"><span class="ic" style="left:0;top:1px;width:8px;height:8px;background:var(--blue)"></span><p class="p" style="font-size:3.4px">Lorem ipsum dolor sit amet, consectetur adipiscing elit, sed do eiusmod tempor incididunt ut labore et dolore magna aliqua minim veniam, quis nostrud.</p></div>
  </div>
</section>

<!-- 15 line chart -->
<section class="slide std">
  <div class="hbrand brand">Norvale</div>
  <h2 class="a" style="left:20px;top:48px;margin:0;font:600 11px/1.25 'Montserrat',sans-serif;color:var(--ink)">This Is Line<br>Chart Slide</h2>
  <div class="a" style="left:24px;top:88px;width:84px;height:8px;background:#7fb3d6;color:#fff;font-size:4px;line-height:8px;text-align:center">CREATIVE TEXT HERE</div>
  <p class="a p" style="left:24px;top:102px;width:80px;color:var(--sky)">Lorem ipsum dolor sit amet, consectetur adipiscing elit, sed do eiusmod tempor incididunt ut labore et commodo consequat dolore magna aliqua.</p>
  <svg width="292" height="165" viewBox="0 0 292 165">
    <g font-family="Open Sans" font-size="3" fill="#8a939b" text-anchor="end">
      <text x="124" y="40">5</text><text x="124" y="49">4.5</text><text x="124" y="58">4</text><text x="124" y="67">3.5</text><text x="124" y="76">3</text><text x="124" y="85">2.5</text><text x="124" y="94">2</text><text x="124" y="103">1.5</text><text x="124" y="112">1</text><text x="124" y="121">0.5</text><text x="124" y="130">0</text>
    </g>
    <g font-family="Open Sans" font-size="3" fill="#8a939b" text-anchor="middle">
      <text x="145" y="136">Category 1</text><text x="182" y="136">Category 2</text><text x="219" y="136">Category 3</text><text x="256" y="136">Category 4</text>
    </g>
    <g fill="none" stroke="#17406d" stroke-width="1.1">
      <polyline points="145,52 182,84 212,57 256,77"/>
      <polyline points="145,82 170,62 199,86 256,52"/>
    </g>
    <g fill="#17406d"><circle cx="145" cy="52" r="1.2"/><circle cx="256" cy="77" r="1.2"/><circle cx="145" cy="82" r="1.2"/><circle cx="256" cy="52" r="1.2"/><circle cx="170" cy="62" r="1.2"/></g>
  </svg>
  <div class="foot">© 2017 NORVALE. All rights reserved</div><div class="corner"></div>
</section>

<!-- 16 brand detailed -->
<section class="slide std">
  <h2 class="title">Brand Detailed</h2><div class="hbrand brand">Norvale</div>
  <div class="ph" role="img" aria-label="City skyline at sunrise" style="left:20px;top:41px;width:134px;height:104px;background:linear-gradient(180deg,#e9d9b8,#9aa4ad 55%,#5f6870)"></div>
  <div class="tile" style="left:156px;top:41px;width:57px;height:52px;background:#6ea7cf"><h4>System</h4><p>Mauris ipsum dolor, cursus at porta et, luctus eget purus. Nunc tempor luctus interdum.</p></div>
  <div class="tile" style="left:215px;top:41px;width:57px;height:52px;background:var(--teal)"><h4>Technology</h4><p>Mauris ipsum dolor, cursus at porta et, luctus eget purus. Nunc tempor luctus interdum.</p></div>
  <div class="tile" style="left:156px;top:95px;width:57px;height:50px;background:#6ea7cf"><h4>Leisure</h4><p>Mauris ipsum dolor, cursus at porta et, luctus eget purus. Nunc tempor luctus interdum.</p></div>
  <div class="tile" style="left:215px;top:95px;width:57px;height:50px;background:var(--teal)"><h4>Digital</h4><p>Mauris ipsum dolor, cursus at porta et, luctus eget purus. Nunc tempor luctus interdum.</p></div>
  <div class="foot">© 2017 NORVALE. All rights reserved</div><div class="corner"></div>
</section>

<!-- 17 title image text -->
<section class="slide std">
  <h2 class="title">Title And Image + Text</h2><div class="hbrand brand">Norvale</div>
  <div class="ph" role="img" aria-label="Colleagues working at computers in an office" style="left:20px;top:33px;width:260px;height:60px;background:linear-gradient(90deg,#7d8893,#c5ced6 50%,#e6eaee)"></div>
  <p class="a" style="left:22px;top:100px;width:126px;margin:0;font-size:6.4px;line-height:1.3;color:var(--ink)">Lorem ipsum dolor sit amet, consectetur adipiscing elit, sed do eiusmod tempor incididunt ut labore et dolore magna aliqua. Ut enimad minim veniam, quis</p>
  <div class="a" style="left:150px;top:100px;width:124px">
    <p class="p" style="font-size:3.3px">Lorem ipsum dolor sit amet, consectetur adipiscing elit, sed do eiusmod tempor incididunt ut labore et dolore magna aliqua. Ut enimad minim veniam, quis nostrud exercitation ullamco laboris nisi ut aliquip ex ea commodo.</p>
    <p class="p" style="font-size:3.3px;margin-top:3px">Duis aute irure dolor in reprehenderit in voluptate velit esse cillum dolore eu fugiat nulla pariatur. Excepteur sint occaecat cupidatat non proident, sunt in culpa qui officia deserunt mollit anim id est laborum.</p>
  </div>
  <div class="foot">© 2017 NORVALE. All rights reserved</div><div class="corner"></div>
</section>

<!-- 18 three bullets -->
<section class="slide std">
  <h2 class="title">Three Bullets Area</h2><div class="hbrand brand">Norvale</div>
  <div class="ph" role="img" aria-label="Smiling team of colleagues in a bright office" style="left:0;top:33px;width:292px;height:62px;background:linear-gradient(90deg,#9aa3ac,#e4e1dc 40%,#c9b9a8 70%,#a7b0b8)"></div>
  <svg width="292" height="165" viewBox="0 0 292 165">
    <circle cx="54" cy="108" r="16" fill="#6ea7cf" stroke="#fff" stroke-width="1.5"/>
    <g stroke="#fff" stroke-width="1" fill="#fff"><circle cx="49" cy="108" r="2"/><circle cx="58" cy="103" r="2"/><circle cx="58" cy="113" r="2"/><path d="M49 108 L58 103 M49 108 L58 113"/></g>
    <circle cx="148" cy="108" r="16" fill="#86cfc6" stroke="#fff" stroke-width="1.5"/>
    <g fill="none" stroke="#fff" stroke-width="1"><path d="M140 105 L148 101 L156 105 L148 109 Z"/><path d="M140 109 L148 113 L156 109"/></g>
    <circle cx="241" cy="108" r="16" fill="#b7babe" stroke="#fff" stroke-width="1.5"/>
    <path d="M236 115 H247 V112 A5.5 7 0 0 0 236 112 Z" fill="#fff"/>
  </svg>
  <p class="a p" style="left:22px;top:128px;width:66px;text-align:center;font-size:3.3px">Lorem ipsum dolor sit amet, consectetur adipiscing elit, sed do eiusmod tempor incididunt ut labore</p>
  <p class="a p" style="left:115px;top:128px;width:66px;text-align:center;font-size:3.3px">Lorem ipsum dolor sit amet, consectetur adipiscing elit, sed do eiusmod tempor incididunt ut labore</p>
  <p class="a p" style="left:208px;top:128px;width:66px;text-align:center;font-size:3.3px">Lorem ipsum dolor sit amet, consectetur adipiscing elit, sed do eiusmod tempor incididunt ut labore</p>
  <div class="foot">© 2017 NORVALE. All rights reserved</div><div class="corner"></div>
</section>

<!-- 19 team investors -->
<section class="slide std">
  <h2 class="title">Team Investors</h2><div class="hbrand brand">Norvale</div>
  <div class="a person" style="left:25px;top:30px;width:95px">
    <div class="ph" role="img" aria-label="Portrait of Marco Delano" style="left:0;top:3px;width:24px;height:30px;background:linear-gradient(#d7dde2,#8f989f)"></div>
    <div style="margin-left:28px"><ul><li>Partner</li><li>Joined Norvale in 2000</li><li>20 years investment banking and technology experience</li><li>Specialising in high growth technology companies</li><li>MBA, Ashford Business School</li></ul></div>
  </div>
  <div class="a person" style="left:133px;top:22px;width:95px">
    <p class="nm">Tomas Brandt</p>
    <div class="ph" role="img" aria-label="Portrait of Tomas Brandt" style="left:0;top:10px;width:24px;height:30px;background:linear-gradient(#d7dde2,#8f989f)"></div>
    <div style="margin-left:28px"><ul><li>Partner</li><li>Joined Norvale in 2000</li><li>21 years investment banking and technology experience</li><li>Corvex Systems, Product Marketing</li><li>BS Degree, Kellmore School of Finance</li></ul></div>
  </div>
  <div class="a person" style="left:25px;top:73px;width:95px">
    <p class="nm">Owen Hale</p>
    <div class="ph" role="img" aria-label="Portrait of Owen Hale" style="left:0;top:10px;width:24px;height:30px;background:linear-gradient(#d7dde2,#8f989f)"></div>
    <div style="margin-left:28px"><ul><li>Finance Director</li><li>Joined Norvale in 2012</li><li>Financial Controller, Venture Partners</li><li>Chartered Accountant</li><li>BSc in Biochemistry</li></ul></div>
  </div>
  <div class="a person" style="left:133px;top:68px;width:95px">
    <p class="nm">Luca Ferrante</p>
    <div class="ph" role="img" aria-label="Portrait of Luca Ferrante" style="left:0;top:10px;width:24px;height:30px;background:linear-gradient(#d7dde2,#8f989f)"></div>
    <div style="margin-left:28px"><ul><li>Principal</li><li>Joined Norvale in 2007</li><li>Leads deal sourcing and investment review process</li><li>Data analytics specialist</li><li>BA Degree, Brightwater College</li></ul></div>
  </div>
  <div class="a person" style="left:25px;top:118px;width:95px">
    <p class="nm">Pieter Vosman</p>
    <div class="ph" role="img" aria-label="Portrait of Pieter Vosman" style="left:0;top:10px;width:24px;height:30px;background:linear-gradient(#d7dde2,#8f989f)"></div>
    <div style="margin-left:28px"><ul><li>Associate</li><li>Joined Norvale in 2014</li><li>Capital markets analyst</li><li>BA, Halvern University</li><li>MBA, Corporate Finance</li></ul></div>
  </div>
  <div class="foot">© 2017 NORVALE. All rights reserved</div><div class="corner"></div>
</section>

<!-- 20 our team -->
<section class="slide std">
  <h2 class="title" style="color:#d08a55">Our Team</h2><div class="hbrand brand">Norvale</div>
  <div class="a person" style="left:20px;top:40px;width:90px">
    <div class="ph" role="img" aria-label="Portrait of Marco Delano" style="left:0;top:0;width:28px;height:28px;border-radius:50%;background:linear-gradient(#dfe4e8,#8f989f)"></div>
    <div style="margin-left:32px"><p class="nm">Marco Delano</p><p class="rl">Partner</p><ul><li>Joined Norvale in 2000</li><li>20 years investment banking and technology experience</li><li>MBA, Ashford Business School</li></ul></div>
  </div>
  <div class="a person" style="left:106px;top:40px;width:90px">
    <div class="ph" role="img" aria-label="Portrait of Tomas Brandt" style="left:0;top:0;width:28px;height:28px;border-radius:50%;background:linear-gradient(#dfe4e8,#8f989f)"></div>
    <div style="margin-left:32px"><p class="nm">Tomas Brandt</p><p class="rl">Partner</p><ul><li>Joined Norvale in 2000</li><li>21 years investment banking and technology experience</li><li>BS Degree, Kellmore School of Finance</li></ul></div>
  </div>
  <div class="a person" style="left:196px;top:36px;width:90px">
    <div class="ph" role="img" aria-label="Portrait of Owen Hale" style="left:0;top:4px;width:28px;height:28px;border-radius:50%;background:linear-gradient(#dfe4e8,#8f989f)"></div>
    <div style="margin-left:32px"><p class="nm">Owen Hale</p><p class="rl">Manager</p><ul><li>Joined Norvale in 2012</li><li>Financial Controller</li><li>Chartered Accountant</li><li>BSc in Biochemistry</li></ul></div>
  </div>
  <div class="a person" style="left:66px;top:108px;width:100px">
    <div class="ph" role="img" aria-label="Portrait of Luca Ferrante" style="left:0;top:6px;width:28px;height:28px;border-radius:50%;background:linear-gradient(#dfe4e8,#8f989f)"></div>
    <div style="margin-left:32px"><p class="nm">Luca Ferrante</p><p class="rl">Principal</p><ul><li>Joined Norvale in 2007</li><li>Leads deal sourcing and investment review</li><li>Data analytics specialist</li></ul></div>
  </div>
  <div class="a person" style="left:170px;top:108px;width:100px">
    <div class="ph" role="img" aria-label="Portrait of Pieter Vosman" style="left:0;top:6px;width:28px;height:28px;border-radius:50%;background:linear-gradient(#dfe4e8,#8f989f)"></div>
    <div style="margin-left:32px"><p class="nm">Pieter Vosman</p><p class="rl">Principal</p><ul><li>Joined Norvale in 2007</li><li>Leads deal sourcing and investment review</li><li>BA, Halvern University</li></ul></div>
  </div>
  <div class="foot">© 2017 NORVALE. All rights reserved</div><div class="corner"></div>
</section>

<!-- 21 thank you -->
<section class="slide" style="background:var(--navy)">
  <svg width="292" height="165" viewBox="0 0 292 165">
    <defs><linearGradient id="g21" x1="0" y1="0" x2="1" y2="1"><stop offset="0" stop-color="#9ec6e2"/><stop offset="1" stop-color="#4f8fc0"/></linearGradient></defs>
    <polygon role="img" aria-label="White steel roof structure tinted blue" points="98,0 292,0 292,165 22,165" fill="url(#g21)"/>
    <polygon points="200,0 292,0 292,165 150,165" fill="#17406d" opacity=".35"/>
    <polygon points="0,0 40,0 0,60" fill="#5c9ccb" opacity=".35"/>
  </svg>
  <div class="a brand" style="left:150px;top:46px;font-size:26px;color:#fff">Norvale</div>
  <div class="a" style="left:140px;width:118px;top:82px;text-align:center;color:#fff">
    <div style="font:600 11px 'Montserrat',sans-serif">THANK YOU</div>
    <div style="font-size:6.4px;font-weight:300">For Your Precious Time</div>
  </div>
</section>

</main>
</body>
</html>
```